Business Card Design Project

We need a business card design for an existing company in Dallas/Fort Worth that is expanding services and re-branding. We are changing the name from Brightmoor Commercial Cleaning to Keystride Facility Services. We are expanding from only commercial cleaning to include complete commercial landscape and facility maintenance services, too.

As stated, we offer a package of services that includes landscape, janitorial and facility services, which is largely unique in the industry.

We would like a design that communicates trust/partnership with a professional, corporate image, but not necessarily using the standard white business card. We would like a design that perhaps uses darker blues or perhaps a gray background, but we are open to other ideas. We might also be interested in a double-sided design - maybe with our logo on the back, printed on a gray background?

We will probably stick with the attached logo, but if you've got another inspired idea....

Target Market(s)

Property managers, commercial real estate professionals, corporate executives

Industry/Entity Type

Landscape

Requirements
Should not have
• Not interested in old style fonts.

```html
<!DOCTYPE html>
<html lang="en">
<head>
<meta charset="utf-8">
<title>Keystride Facility Services – Business Card</title>
<link rel="stylesheet" href="https://fonts.googleapis.com/css2?family=Dosis:wght@400;500;600;700&display=swap">
<style>
  :root {
    --backdrop: #3c403f;
    --card-white: #f4f4f4;
    --card-shade: #e2e2e2;
    --ink-dark: #3d3d3f;
    --ink-mid: #555558;
    --brand-purple: #4b3f8f;
    --stripe-gray: #4a4a4d;
    --back-gray: #4b4b4e;
    --back-gray-deep: #3f3f42;
    --on-dark: #f2f2f2;
  }
  * { box-sizing: border-box; margin: 0; padding: 0; }
  html, body { width: 1200px; height: 900px; overflow: hidden; }
  body {
    background: var(--backdrop);
    font-family: "Dosis", sans-serif;
    display: flex;
    flex-direction: column;
    align-items: center;
    justify-content: center;
    gap: 60px;
  }
  .card {
    position: relative;
    width: 560px;
    height: 320px;
    overflow: hidden;
    box-shadow: 0 10px 30px rgba(0,0,0,.35);
  }

  /* Front */
  .card-front {
    background: linear-gradient(135deg, var(--card-white) 0%, var(--card-white) 55%, var(--card-shade) 100%);
    color: var(--ink-dark);
  }
  .brand {
    position: absolute;
    left: 36px;
    top: 34px;
    display: flex;
    align-items: center;
    gap: 14px;
  }
  .brand-square {
    width: 62px;
    height: 62px;
    border: 6px solid var(--brand-purple);
  }
  .brand-name {
    font-weight: 600;
    font-size: 25px;
    line-height: 1.05;
    letter-spacing: 2px;
    text-transform: uppercase;
    color: var(--ink-dark);
  }
  .brand-tagline {
    margin-top: 4px;
    font-size: 10.5px;
    font-weight: 600;
    font-style: italic;
    color: var(--brand-purple);
    letter-spacing: .2px;
    text-transform: none;
  }
  .person {
    position: absolute;
    right: 40px;
    top: 150px;
    text-align: right;
  }
  .person-name { font-size: 20px; font-weight: 600; color: var(--ink-dark); }
  .person-title { font-size: 14px; font-weight: 500; color: var(--brand-purple); margin-top: 2px; }
  .person-cell { font-size: 13px; font-weight: 500; color: var(--ink-mid); margin-top: 2px; }

  .contact {
    position: absolute;
    left: 36px;
    top: 190px;
    font-size: 12.5px;
    font-weight: 600;
    color: var(--ink-mid);
    line-height: 1.4;
  }
  .contact-line { display: flex; align-items: center; gap: 5px; }
  .contact-line svg { width: 11px; height: 11px; fill: var(--brand-purple); }
  .contact-phones { gap: 4px; }

  .footer-bands {
    position: absolute;
    left: 0;
    bottom: 0;
    width: 560px;
    height: 64px;
  }
  .footer-web {
    position: absolute;
    right: 24px;
    bottom: 26px;
    font-size: 13px;
    font-weight: 500;
    color: var(--on-dark);
  }

  /* Back */
  .card-back {
    background: linear-gradient(160deg, var(--back-gray) 0%, var(--back-gray-deep) 100%);
    color: var(--on-dark);
  }
  .back-brand {
    position: absolute;
    left: 50%;
    top: 44%;
    transform: translate(-50%, -50%);
    display: flex;
    align-items: center;
    gap: 14px;
  }
  .back-square {
    width: 60px;
    height: 60px;
    border: 6px solid var(--on-dark);
  }
  .back-name {
    font-size: 22px;
    font-weight: 600;
    letter-spacing: 2px;
    text-transform: uppercase;
    line-height: 1.1;
  }
  .back-web {
    position: absolute;
    right: 30px;
    bottom: 28px;
    font-size: 13px;
    font-weight: 500;
  }
</style>
</head>
<body>

  <article class="card card-front">
    <div class="brand">
      <div class="brand-square"></div>
      <div>
        <div class="brand-name">Keystride<br>Facility Services</div>
        <div class="brand-tagline">One Source For Landscape, Janitorial and Facility Maintenance</div>
      </div>
    </div>

    <div class="person">
      <div class="person-name">Dale Morrow</div>
      <div class="person-title">General Manager</div>
      <div class="person-cell">Cell: 972-555-0123</div>
    </div>

    <div class="contact">
      <div>2865 Ridgeline Parkway,</div>
      <div>Fort Worth, TX 76155</div>
      <div class="contact-line contact-phones">
        <svg viewBox="0 0 12 12" aria-hidden="true"><path d="M1 3.5C1 2 2 1 3 1h6c1 0 2 1 2 2.5L9 4.5 8 3H4L3 4.5zM2.5 6l1.5-2h4l1.5 2v4h-7z"/></svg>
        <span>817-555-0142</span>
        <svg viewBox="0 0 12 12" aria-hidden="true"><path d="M2 2h8v8H2zM3 4l3 3 3-3v5H3z"/></svg>
        <span>817-555-0187</span>
      </div>
      <div class="contact-line">
        <svg viewBox="0 0 12 12" aria-hidden="true"><path d="M1 3h10v6H1zM1.5 3.5 6 7l4.5-3.5"/></svg>
        <span>dale@keystridefacilityservices.com</span>
      </div>
    </div>

    <svg class="footer-bands" viewBox="0 0 560 64" aria-hidden="true">
      <polygon points="0,40 330,40 350,22 560,22 560,12 340,12 320,30 0,30" fill="var(--stripe-gray)"/>
      <polygon points="0,64 0,48 340,48 360,14 560,14 560,64" fill="var(--brand-purple)"/>
    </svg>
    <div class="footer-web">www.keystridefacilityservices.com</div>
  </article>

  <article class="card card-back">
    <div class="back-brand">
      <div class="back-square"></div>
      <div class="back-name">Keystride<br>Facility Services</div>
    </div>
    <div class="back-web">www.keystridefacilityservices.com</div>
  </article>

</body>
</html>
```